Norwegian psychologist service needs a fresh and exiting web site*

Norwegian psychologist service: working with therapy, personal development, mastery and personal growth. Focus: children and teenagers with special needs; family dynamics; group processes; individuals with a need for therapy and personal growth. (Our company name: Fjordlys og samhold (means Mastery and Growth).

We already have a logo for the company, which will be used (will be attached in the project).

The webside is to be structured in 4 pages with roll down curtain menus (the numbers are just for guiding the designer - the should not be added):

Page 1: Om Fjordlys og Samhold (about Mastery and Growth): this is where our business is is presented/described shortly: Lorem Ipsum dolor cit...

Page 2: Tjenester (Services): this is where our 5 service areas are presented:
2.1 Utredning (Investigation, diagnosing): Lorem Ipsum dolor cit...
2.2 Rådgivning (consulting): Lorem Ipsum dolor cit...

2.3 Kurs og work shops (courses and work shops): Lorem Ipsum dolor cit...
2.3a Fjordlys og samhold Tema 1 (T1)
2.3b Fjordlys og samhold Tema 2 (T2)
2.3c Fjordlys og samhold Tema 3 (T3)

2.4 Terapi og utvikling (Therapy and development)
2.4a Fjordlys og samhold for individer (FS1)
2.4b Fjordlys og samhold i familier (FS2)
2.4c Fjordlys og samhold i grupper (FS3)
2.4d Fjordlys og samhold i institusjoner (FS4)

Page 3: Aktuelt (Blog): this is our blog where we share knowledge and articles

Page 4: Kontakt (Contact): This is the contact form page. Contact form should constitute:
- Ditt navn (your name)
- E-post (your e-mail)
- Emne (subject)
- Melding (message/description)

Our project should also include suggestion for handheld units (iPhone, iPad).
Updates

We have both been traveling with work for a while, and then unfortunately both of us got sick on return, so we need a few more days to evaluate and choose design. Kind Regards Arvid & Margit

Target Market(s)

Focus on therapy, learning, mastery and growth for children and teenagers with special needs, within the family dynamics, or in a group setting.
OUR MARKETS:
Private market: individuals, families, groups and health industry institutions (with focus on learning, mastery, growth (as well as growing up) and psychiatry for children and teenagers with special difficulties and needs)
Public institutions: Government institutions, state institutions and municipality institutions (e.g. schools, municipality health service, hospitals) that serve the public (families with children and teenagers with special needs, and where learning, mastery, growth (as well as growing up) and potential psychiatry is an issue).

Number of Pages Required

4 page

Font styles to use
Sans Serif

Colors

Designer to choose colors to be used in the design.

Requirements
Must have
• The website must have 4 pages with roll down curtain menus (we have added a PDF with suggested structure, and headings, with sub menus - see attached PDF drawing.
• The web page must also use the added logo file - and make the web page work well with our logo.
• We would like the website to have a modern look and we would like the site to be associated with typical HIGH END TOP QUALITY private health institutions, but with a stronger focus on human beings (hands, faces etc), and not white coats and doctors. We are psychologists in the private market.
• For instance, if photos are being used - we tend to like "warm" almost art-like, "grainy" two-tone (e.g. sepia) photos to illustrate our focus. If designer can find such photos as part of design, it would be interesting to us. We would like a few photos like that integrated in the design.
• We also want a design suggestion for how the web page should look like and behave on handheld units (e.g. iPhone, iPad).
Nice to have
• If designer could find a number of suitable photos that matches the business idea and design requirements (see description above), that could follow website, that would be good.
• It could also be nice to have graphic symbols that denote the different pages/subpages (subjects)....
• HORSES: we sometimes use horses as a "tool" in therapy sessions. The horse is not necessarily used for riding, but for contact, communication and grooming. PHOTOS: we would like the designer to find an opportunity for using a photo reflecting this cooperation between therapist, child, teenager and horse. It is a bit up to the designer to find a way to do this... Since the horse is only a tool, among many other tools, it does not have to be much - but we want to try and see how it will work with a photo that also reflects this part of our business.

```html
<!DOCTYPE html>
<html lang="no">
<head>
<meta charset="utf-8">
<title>Fjordlys og Samhold – Tjenester</title>
<link href="https://fonts.googleapis.com/css2?family=Fira+Sans:wght@400;700&family=Fira+Sans+Condensed:wght@400&family=Lato:wght@300&display=swap" rel="stylesheet">
<style>
  :root{
    --purple:#821ac9;
    --heading:#7d22c6;
    --navy:#2b3a8a;
    --gold:#c9891f;
    --body:#7a7a7a;
    --white:#ffffff;
  }
  *{margin:0;padding:0;box-sizing:border-box}
  html,body{width:808px;height:1200px;overflow:hidden;background:var(--white)}
  .page{position:relative;width:808px;height:1200px}
  .site-header{position:absolute;left:0;top:0;width:808px;height:78px;display:flex;align-items:center;justify-content:center;gap:8px}
  .brand-mark{width:14px;height:14px;border-radius:50%;background:var(--navy)}
  .brand-name{font-family:"Fira Sans",sans-serif;font-weight:400;font-size:17px;letter-spacing:.5px;color:var(--navy)}
  .main-nav{position:absolute;left:0;top:78px;width:808px;height:36px;background:var(--purple)}
  .nav-item{position:absolute;top:8px;transform:translateX(-50%);font-family:"Fira Sans",sans-serif;font-weight:700;font-size:13px;color:var(--white);white-space:nowrap}
  .nav-icon{position:absolute;top:106px;width:26px;height:26px;margin-left:-13px;border-radius:50%;background:var(--white);display:flex;align-items:center;justify-content:center;z-index:2}
  .nav-icon.active{background:var(--purple);border:2px solid var(--white)}
  .hero{position:absolute;left:0;top:114px;width:808px;height:106px;background:linear-gradient(90deg,#b9a48c 0%,#d8cfc4 25%,#c7b6a6 48%,#cbb39a 56%,#8a8c9a 70%,#7d7f8e 100%)}
  .service-photo{position:absolute;width:230px;height:230px}
  .service-title{position:absolute;font-family:"Fira Sans",sans-serif;font-weight:400;font-size:23.5px;color:var(--heading);white-space:nowrap;line-height:1}
  .service-text{position:absolute;width:228px;font-family:"Lato",sans-serif;font-weight:300;font-size:8.2px;line-height:13.1px;color:var(--body)}
  .more-button{position:absolute;width:150px;height:28px;background:var(--gold);color:var(--white);font-family:"Fira Sans Condensed",sans-serif;font-size:13px;display:flex;align-items:center;justify-content:center}
  .site-footer{position:absolute;left:0;top:1140px;width:808px;height:60px;background:var(--purple)}
  .copyright{position:absolute;top:13px;width:808px;text-align:center;font-family:"Lato",sans-serif;font-weight:300;font-size:8.5px;color:var(--white)}
  .social{position:absolute;top:35px;width:12px;height:12px;border:1.4px solid var(--white);border-radius:50%}
</style>
</head>
<body>
<div class="page">
  <header class="site-header">
    <span class="brand-mark"></span>
    <span class="brand-name">Fjordlys og Samhold</span>
  </header>

  <nav class="main-nav">
    <span class="nav-item" style="left:268px">Om Fjordlys og Samhold</span>
    <span class="nav-item" style="left:402px">Tjenester</span>
    <span class="nav-item" style="left:491px">Aktuelt</span>
    <span class="nav-item" style="left:578px">Kontakt</span>
  </nav>

  <div class="hero" role="img" aria-label="Nærbilde av en voksen som holder et barn i hånden"></div>

  <span class="nav-icon" style="left:274px"><svg width="14" height="14" viewBox="0 0 14 14" fill="none" stroke="#821ac9" stroke-width="1"><path d="M2 10c2 0 3-1 5-1s3 1 5 0"/><path d="M7 9V5"/><path d="M7 5c-2 0-3-1-3-3 2 0 3 1 3 3zM7 6c1.5 0 2.5-1 2.5-2.5C8 3.5 7 4.5 7 6z"/></svg></span>
  <span class="nav-icon active" style="left:402px"><svg width="14" height="14" viewBox="0 0 14 14" fill="none" stroke="#fff" stroke-width="1"><circle cx="7" cy="7" r="5.5"/><circle cx="7" cy="7" r="3"/><circle cx="7" cy="7" r="1"/></svg></span>
  <span class="nav-icon" style="left:490px"><svg width="14" height="14" viewBox="0 0 14 14" fill="none" stroke="#821ac9" stroke-width="1"><path d="M3 11l1-3 6-6 2 2-6 6z"/><path d="M2 12h10"/></svg></span>
  <span class="nav-icon" style="left:577px"><svg width="14" height="14" viewBox="0 0 14 14" fill="none" stroke="#821ac9" stroke-width="1"><rect x="2" y="3.5" width="10" height="7" rx="1"/><path d="M2 4l5 4 5-4"/></svg></span>

  <div class="service-photo" style="left:49px;top:261px;background:linear-gradient(135deg,#b9573a,#d9d2c8 55%,#e8e6e2)" role="img" aria-label="Fagperson leser gjennom papirer ved en datamaskin"></div>
  <div class="service-photo" style="left:289px;top:261px;background:linear-gradient(135deg,#a9c0d8,#5a3a2c 45%,#2f8fb8 75%,#b4cc5a)" role="img" aria-label="Familie som leser sammen med en rådgiver"></div>
  <div class="service-photo" style="left:529px;top:261px;background:radial-gradient(circle at 35% 30%,#c98a4a,#3b3a3e 55%,#242730)" role="img" aria-label="Hånd som holder en lyspære mot et lysende bakgrunnslys"></div>

  <h2 class="service-title" style="left:49px;top:503px">Utredning</h2>
  <h2 class="service-title" style="left:287px;top:503px">Rådgivning</h2>
  <h2 class="service-title" style="left:528px;top:503px">Kurs og workshops</h2>

  <p class="service-text" style="left:49px;top:533px">Lorem ipsum dolor sit amet, consectetur adipiscing elit. Nunc auctor, lectus in ultrices semper, sapien mi venenatis mauris, id consectetur tortor dolor in mauris. Nunc porttitor massa vel sagittis lobortis. Aenean molestie lacinia mauris non bibendum. Nullam in mi eleifend, suscipit lorem ut, luctus sapien. Mauris id sapien eu ante vestibulum viverra. Cras auctor mi at nulla dictum mollis. Quisque faucibus sem magna, ut finibus orci fringilla id.</p>
  <p class="service-text" style="left:290px;top:533px">Lorem ipsum dolor sit amet, consectetur adipiscing elit. Nunc auctor, lectus in ultrices semper, sapien mi venenatis mauris, id consectetur tortor dolor in mauris. Nunc porttitor massa vel sagittis lobortis. Aenean molestie lacinia mauris non bibendum. Nullam in mi eleifend, suscipit lorem ut, luctus sapien. Mauris id sapien eu ante vestibulum viverra. Cras auctor mi at nulla dictum mollis. Quisque faucibus sem magna, ut finibus orci fringilla id.</p>
  <p class="service-text" style="left:528px;top:533px">Lorem ipsum dolor sit amet, consectetur adipiscing elit. Nunc auctor, lectus in ultrices semper, sapien mi venenatis mauris, id consectetur tortor dolor in mauris. Nunc porttitor massa vel sagittis lobortis. Aenean molestie lacinia mauris non bibendum. Nullam in mi eleifend, suscipit lorem ut, luctus sapien. Mauris id sapien eu ante vestibulum viverra. Cras auctor mi at nulla dictum mollis. Quisque faucibus sem magna, ut finibus orci fringilla id.</p>

  <a class="more-button" style="left:89px;top:638px">vite mer</a>
  <a class="more-button" style="left:329px;top:638px">vite mer</a>
  <a class="more-button" style="left:569px;top:638px">vite mer</a>

  <div class="service-photo" style="left:139px;top:694px;background:linear-gradient(180deg,#9fb0c4,#c5ced8 60%,#aebdcc)" role="img" aria-label="To hender som strekker seg mot hverandre mot en lys himmel"></div>
  <div class="service-photo" style="left:439px;top:694px;background:radial-gradient(circle at 50% 45%,#b8ab94,#6f6554 55%,#1e1b17)" role="img" aria-label="Sepiafarget bilde av to tredukker som omfavner hverandre"></div>

  <h2 class="service-title" style="left:137px;top:943px">Terapi og utvikling</h2>
  <h2 class="service-title" style="left:439px;top:943px">service 5</h2>

  <p class="service-text" style="left:137px;top:973px">Lorem ipsum dolor sit amet, consectetur adipiscing elit. Nunc auctor, lectus in ultrices semper, sapien mi venenatis mauris, id consectetur tortor dolor in mauris. Nunc porttitor massa vel sagittis lobortis. Aenean molestie lacinia mauris non bibendum. Nullam in mi eleifend, suscipit lorem ut, luctus sapien. Mauris id sapien eu ante vestibulum viverra. Cras auctor mi at nulla dictum mollis. Quisque faucibus sem magna, ut finibus orci fringilla id.</p>
  <p class="service-text" style="left:439px;top:973px">Lorem ipsum dolor sit amet, consectetur adipiscing elit. Nunc auctor, lectus in ultrices semper, sapien mi venenatis mauris, id consectetur tortor dolor in mauris. Nunc porttitor massa vel sagittis lobortis. Aenean molestie lacinia mauris non bibendum. Nullam in mi eleifend, suscipit lorem ut, luctus sapien. Mauris id sapien eu ante vestibulum viverra. Cras auctor mi at nulla dictum mollis. Quisque faucibus sem magna, ut finibus orci fringilla id.</p>

  <a class="more-button" style="left:179px;top:1080px">vite mer</a>
  <a class="more-button" style="left:480px;top:1080px">vite mer</a>

  <footer class="site-footer">
    <p class="copyright">Copy Right 2020 @ Your Company - ETC</p>
    <span class="social" style="left:365px"></span>
    <span class="social" style="left:396px"></span>
    <span class="social" style="left:428px"></span>
  </footer>
</div>
</body>
</html>
```